Mixed Martial Arts gym that is known for high quality athletes, students and training

We need a business card designed that is unique and stands out. Something that is not so dark and boring but looks 'energetic' to those that are given it. The customers that would receive this card would be looking to sign up for martial arts or fitness training and this card is used for corporate sponsorships and networking as well.

Marcus Pellow-Grant
0417305962 or 0409561738
Level 1, 284 Wendover Road. Halvern NSW 2197
marcus@kinetiqcombatworks.com.au
www.kinetiqcombatworks.com

```html
<!DOCTYPE html>
<html lang="en">
<head>
<meta charset="utf-8">
<title>Kinetiq Combat Works – Business Card</title>
<link href="https://fonts.googleapis.com/css2?family=Open+Sans:wght@400;600;700&display=swap" rel="stylesheet">
<style>
  :root {
    --backdrop: #9a7550;
    --card-white: #ffffff;
    --brand-orange: #f7941d;
    --bar-grey: #58595b;
    --ink-dark: #3b2b1c;
    --ink-white: #ffffff;
  }
  * { box-sizing: border-box; margin: 0; padding: 0; }
  html, body {
    width: 1115px;
    height: 1200px;
    overflow: hidden;
    background: var(--backdrop);
    font-family: "Open Sans", Arial, sans-serif;
  }
  .canvas { position: relative; width: 1115px; height: 1200px; }

  .card {
    position: absolute;
    left: 92px;
    width: 877px;
    height: 500px;
  }
  .card-front { top: 45px; background: var(--card-white); }
  .card-back  { top: 598px; background: var(--brand-orange); }

  /* Front: brand name */
  .front-brand {
    position: absolute;
    left: 60px;
    top: 182px;
    width: 330px;
    text-align: center;
    color: var(--brand-orange);
    font-weight: 700;
    font-size: 40px;
    line-height: 1.1;
    text-transform: uppercase;
    letter-spacing: 1px;
  }

  /* Front: vertical web bar */
  .web-bar {
    position: absolute;
    left: 402px;
    top: 72px;
    width: 47px;
    height: 353px;
    background: var(--bar-grey);
  }
  .web-bar .web-address {
    position: absolute;
    left: 50%;
    top: 50%;
    transform: translate(-50%, -50%) rotate(-90deg);
    white-space: nowrap;
    color: var(--ink-white);
    font-size: 17px;
    font-weight: 400;
  }

  /* Front: contact panel */
  .contact-panel {
    position: absolute;
    left: 459px;
    top: 72px;
    width: 418px;
    height: 353px;
    background: var(--brand-orange);
    color: var(--ink-dark);
  }
  .contact-name {
    position: absolute;
    left: 20px;
    top: 66px;
    font-size: 28px;
    font-weight: 700;
  }
  .contact-line {
    position: absolute;
    left: 20px;
    display: flex;
    align-items: flex-start;
    font-size: 20px;
    line-height: 30px;
  }
  .contact-line svg { width: 18px; height: 22px; margin: 4px 14px 0 4px; flex: none; fill: var(--ink-dark); }
  .contact-phone { top: 130px; }
  .contact-email { top: 173px; font-size: 19px; }
  .contact-address { top: 220px; }

  /* Back: brand name */
  .back-brand {
    position: absolute;
    left: 0;
    right: 0;
    top: 160px;
    text-align: center;
    color: var(--ink-white);
    font-weight: 700;
    font-size: 84px;
    line-height: 1.05;
    text-transform: uppercase;
    letter-spacing: 2px;
  }
</style>
</head>
<body>
<main class="canvas">

  <section class="card card-front" aria-label="Business card front">
    <div class="front-brand">Kinetiq<br>Combat Works</div>

    <div class="web-bar">
      <span class="web-address">www.kinetiqcombatworks.com</span>
    </div>

    <div class="contact-panel">
      <h1 class="contact-name">Marcus Pellow-Grant</h1>

      <p class="contact-line contact-phone">
        <svg viewBox="0 0 18 22" aria-hidden="true"><path d="M4 1 L8 1 L8 7 L6 8 C6 11 7 14 9 16 L11 15 L14 19 L11 21 C5 19 1 11 2 4 Z"/></svg>
        0417305962
      </p>

      <p class="contact-line contact-email">
        <svg viewBox="0 0 18 22" aria-hidden="true"><path d="M1 6 H17 V18 H1 Z M2 7 L9 13 L16 7" fill="none" stroke="#3b2b1c" stroke-width="2"/></svg>
        marcus@kinetiqcombatworks.com.au
      </p>

      <p class="contact-line contact-address">
        <svg viewBox="0 0 18 22" aria-hidden="true"><path d="M9 1 C4 1 1 4.5 1 8.5 C1 14 9 21 9 21 C9 21 17 14 17 8.5 C17 4.5 14 1 9 1 Z M9 5.5 A3 3 0 1 0 9 11.5 A3 3 0 1 0 9 5.5 Z" fill-rule="evenodd"/></svg>
        <span>Suite 4, 284 Wendover Road<br>Halvern NSW 2197</span>
      </p>
    </div>
  </section>

  <section class="card card-back" aria-label="Business card back">
    <div class="back-brand">Kinetiq<br>Combat Works</div>
  </section>

</main>
</body>
</html>
```